Update our business cards to match our awesome new website

Need a new design for company business cards. We have recently revamped our website and would like our business cards to get a refresh too. I've uploaded the company artwork, logo, as well as the Branding Deck to better understand the look & feel of our brand. Please visit the website at bellcrestholdingsoh.com.

Industry/Entity Type

Real Estate

Contact Information for Business Card

must use the colors outlined in the Branding Deck uploaded to the site, or the colors of our logo.

Font styles to use
Other font styles liked:
• Calibri

Requirements
Must have
• Required items: Name, title, company logo, address: 217 Fennimore Ave. Suite 300, Lakeport, OH 44093, email address: glen@bellcrestholdingsOH.com, company phone 800-555-0172, cell: 216-555-0148
Nice to have
• a more simple design. not complicated
Should not have
• cartoonish characters, or whimsical writing or artwork, stay within our branding colors

```html
<!DOCTYPE html>
<html lang="en">
<head>
<meta charset="utf-8">
<title>Bellcrest Holdings – Business Card</title>
<link rel="stylesheet" href="https://fonts.googleapis.com/css2?family=Carlito:wght@400;700&display=swap">
<style>
  :root {
    --backdrop: #e3e3e3;
    --card: #f4f4f4;
    --ink: #2a2a2a;
    --ink-soft: #333333;
    --accent-green: #1f9e6c;
    --accent-blue: #3a8fd0;
    --brand-sun: #f07a22;
    --rule: #3a3a3a;
  }
  * { box-sizing: border-box; margin: 0; padding: 0; }
  html, body {
    width: 1200px; height: 960px; overflow: hidden;
    background: var(--backdrop);
    font-family: "Carlito", "Calibri", sans-serif;
    color: var(--ink);
  }
  .canvas { position: relative; width: 1200px; height: 960px; }
  .card {
    position: absolute; left: 302px; width: 595px; height: 340px;
    background: var(--card);
  }
  .card--front { top: 115px; }
  .card--back { top: 508px; }

  .brand {
    position: absolute; display: flex; align-items: center; gap: 10px;
    color: var(--ink); font-weight: 400; white-space: nowrap;
  }
  .brand__mark { border-radius: 50%; background: var(--accent-green); flex: none; }
  .card--front .brand { left: 0; right: 0; top: 168px; justify-content: center; font-size: 40px; }
  .card--front .brand__mark { width: 22px; height: 22px; }
  .card--back .brand { left: 30px; top: 180px; font-size: 25px; }
  .card--back .brand__mark { width: 14px; height: 14px; }

  .divider {
    position: absolute; left: 297px; top: 104px; width: 1px; height: 133px;
    background: var(--rule);
  }
  .contact { position: absolute; left: 315px; top: 103px; }
  .contact__name { font-size: 19px; font-weight: 700; color: var(--accent-green); line-height: 22px; }
  .contact__title { font-size: 15px; color: var(--ink-soft); line-height: 20px; }
  .contact__list { list-style: none; margin-top: 13px; }
  .contact__item {
    display: flex; align-items: center; gap: 5px;
    font-size: 15px; line-height: 20px; color: var(--ink-soft);
  }
  .contact__item svg { width: 13px; height: 13px; flex: none; }
  .address {
    position: absolute; left: 0; right: 0; top: 294px; text-align: center;
    font-size: 15px; color: var(--ink-soft);
  }
</style>
</head>
<body>
<main class="canvas">
  <section class="card card--front" aria-label="Card front">
    <div class="brand"><span class="brand__mark"></span><span class="brand__name">Bellcrest Holdings</span></div>
  </section>

  <section class="card card--back" aria-label="Card back">
    <div class="brand"><span class="brand__mark"></span><span class="brand__name">Bellcrest Holdings</span></div>
    <div class="divider"></div>
    <div class="contact">
      <p class="contact__name">Glen Marlowe</p>
      <p class="contact__title">President</p>
      <ul class="contact__list">
        <li class="contact__item">
          <svg viewBox="0 0 16 16" aria-hidden="true"><path fill="var(--accent-blue)" d="M3.5 1l2.5 3-1.5 2c1 2 3 4 5 5l2-1.5 3 2.5-1.5 2.5C7 15 1 9 1 2.5z"/></svg>
          <span>800-555-0172</span>
        </li>
        <li class="contact__item">
          <svg viewBox="0 0 16 16" aria-hidden="true"><rect x="4" y="1" width="8" height="14" rx="1.5" fill="none" stroke="var(--accent-blue)" stroke-width="1.5"/><circle cx="8" cy="12.5" r="0.9" fill="var(--accent-blue)"/></svg>
          <span>216-555-0148</span>
        </li>
        <li class="contact__item">
          <svg viewBox="0 0 16 16" aria-hidden="true"><rect x="1" y="3" width="14" height="10" fill="none" stroke="var(--accent-blue)" stroke-width="1.4"/><path d="M1 3l7 6 7-6" fill="none" stroke="var(--accent-blue)" stroke-width="1.4"/></svg>
          <span>glen@bellcrestholdingsOH.com</span>
        </li>
        <li class="contact__item">
          <svg viewBox="0 0 16 16" aria-hidden="true"><g fill="none" stroke="var(--accent-blue)" stroke-width="1.2"><circle cx="8" cy="8" r="6.5"/><ellipse cx="8" cy="8" rx="3" ry="6.5"/><path d="M1.5 8h13M2.5 4.5h11M2.5 11.5h11"/></g></svg>
          <span>www.bellcrestholdingsOH.com</span>
        </li>
      </ul>
    </div>
    <p class="address">217 Fennimore Ave. Suite 300, Lakeport, OH 44093</p>
  </section>
</main>
</body>
</html>
```